**Designs Wanted for High Profile Banner Ad Campaign**

Our leading Public Relations agency services some of the world's leading brands in our local market.

We now need a banner ad design to support our own growth.

We are looking to have banner ads designed that will carry a common theme to be used across the following sizes (all these sizes will need to be created):
• Vertical rectangle: 240 x 400
• Mobile leaderboard: 320 x 50
• Banner: 468 x 60
• Leaderboard: 728 x 90
• Square: 250 x 250
• Small square: 200 x 200
• Large rectangle: 336 x 280
• Inline rectangle: 300 x 250
• Skyscraper: 120 x 600
• Wide skyscraper: 160 x 600
• Half-page: 300 x 600
• Large leaderboard: 970x90
• Large mobile banner: 320 x 100
• Billboard: 970 x 250

Our primary retargeting and regular display campaign objective is to encourage marketing managers and business owners to visit our site and contact us.
See www.lumenvale.co.nz for our current look and feel. Please keep consistent colours with that site. Our two logos are attached.

This is our first digital retargeting campaign and we are open to your advice and suggestions on what will encourage click through from potential clients.

Our current thinking at the moment is that the ad could be built around these concepts:
“Reach, socialise, inspire.”
In others words – as a PR agency we help clients ‘reach’ their target market through creating content for news media.
The ‘socialise’ represents engagement through social media – in that we help develop and build their social media presence.
‘Inspire’ refers to the fact we aim to inspire their target market towards engaging with our clients.
Plus a suitable call to action– eg. Click here to meet your public relations needs today.

In terms of designs we are open to suggestion: eg. the adverts could use icons or something else that you have seen work.

We would like to see some eye catching animation, interaction or movement in the advert to.

We need the ad to be effective, eye catching, professional, modern, sophisticated (in that our target market is professional executives) and crisp, clean and uncluttered.

Time is short for us, so please send through designs as soon as possible – don’t wait until the last day!

Additional note: the existing fish image and 'stand out from the crowd' slogan on our home page are not required as part of this design. We have been looking to move towards the new slogan (“Reach, socialise, inspire.” ) and this banner ad may also serve to give us some new direction ideas as well. we do need to keep the existing logo and orange colour though.

Target Market(s)

Business to Business. Marketing and brand managers, Small, Medium and large business owners and executives.
Those with a business in the New Zealand market.

Industry/Entity Type

Marketing

Requirements
Must have
• our logo
animation or movement
orange colour/ consistency with our existing website.
our proposed slogan: “Reach, socialise, inspire.” (however we are open to seeing alternative ideas as well if you want to submit more than one concept)
call to action.
Should not have
• read note about existing fish and slogan above.

```html
<!DOCTYPE html>
<html lang="en">
<head>
<meta charset="utf-8">
<title>Lumenvale – Reach, Socialise, Inspire banner set</title>
<link rel="stylesheet" href="https://fonts.googleapis.com/css2?family=Lato:wght@300;400;700;900&display=swap">
<style>
  :root {
    --orange: #f26522;
    --orange-deep: #d9460f;
    --orange-light: #f7894f;
    --tint: #f9b690;
    --ink: #1e1e1e;
    --frame: #8a8a8a;
    --base-top: #e3e3e3;
    --base-bottom: #ffffff;
    --page: #ffffff;
  }
  * { box-sizing: border-box; margin: 0; padding: 0; }
  html, body { width: 1200px; height: 556px; overflow: hidden; background: var(--page); }
  body { font-family: "Lato", Arial, sans-serif; }
  .banner-set { position: relative; width: 1200px; height: 556px; }
  .banner {
    position: absolute; top: 10px; width: 285px; height: 537px;
    border: 1px solid var(--frame); background: var(--page);
    display: flex; flex-direction: column;
  }
  .banner--reach { left: 15px; }
  .banner--socialise { left: 309px; }
  .banner--inspire { left: 603px; }
  .banner--cta { left: 897px; }
  .banner__stage { position: relative; height: 362px; }
  .banner__word {
    position: absolute; top: 48px; left: 0; right: 0; text-align: center;
    font-weight: 300; font-size: 48px; letter-spacing: 1px; color: var(--ink); line-height: 1;
  }
  .icon-tile {
    position: absolute; top: 155px; left: 28px; width: 229px; height: 166px;
    border-radius: 36px;
    background: linear-gradient(160deg, var(--orange-light) 0%, var(--orange) 45%, var(--orange-deep) 100%);
    border: 2px solid #c43d0c;
    box-shadow: 0 14px 10px -8px rgba(0,0,0,.35);
    overflow: hidden;
  }
  .icon-tile::before {
    content: ""; position: absolute; left: 0; right: 0; top: 0; height: 48%;
    background: linear-gradient(rgba(255,255,255,.28), rgba(255,255,255,0));
    border-radius: 34px 34px 60% 60% / 34px 34px 22px 22px;
  }
  .icon-tile__art {
    position: absolute; left: 30px; right: 30px; top: 22px; bottom: 18px;
    border-radius: 20px;
    background: linear-gradient(180deg, rgba(249,182,144,.85), rgba(249,182,144,.35));
  }
  .icon-tile svg { position: absolute; left: 0; top: 0; }
  .banner__base {
    flex: 1; border-top: 1px solid #cfcfcf;
    background: linear-gradient(var(--base-top), var(--base-bottom));
    display: flex; align-items: center; justify-content: center;
  }
  .brand-name {
    font-weight: 700; font-size: 40px; letter-spacing: 1px; color: var(--orange); line-height: 1;
  }
  .cta__lead {
    position: absolute; top: 38px; left: 0; right: 0; text-align: center;
    font-weight: 400; font-size: 27px; line-height: 1.15; color: var(--ink);
  }
  .cta__headline {
    position: absolute; top: 106px; left: 0; right: 0; text-align: center;
    font-weight: 900; font-size: 35px; line-height: 1.08; color: var(--orange);
  }
  .cta__button {
    position: absolute; top: 240px; left: 31px; width: 222px; height: 78px;
    border-radius: 14px; border: 2px solid #c43d0c;
    background: linear-gradient(180deg, var(--orange-light), var(--orange) 50%, var(--orange-deep));
    box-shadow: 0 12px 8px -7px rgba(0,0,0,.35);
    display: flex; align-items: center; justify-content: center;
    color: #fff; font-weight: 700; font-size: 26px; letter-spacing: .5px;
    text-decoration: none;
  }
</style>
</head>
<body>
<main class="banner-set">
  <section class="banner banner--reach">
    <div class="banner__stage">
      <h2 class="banner__word">REACH</h2>
      <div class="icon-tile">
        <div class="icon-tile__art" role="img" aria-label="Illustration of many raised hands reaching upward"></div>
      </div>
    </div>
    <div class="banner__base"><span class="brand-name">LUMENVALE</span></div>
  </section>

  <section class="banner banner--socialise">
    <div class="banner__stage">
      <h2 class="banner__word">SOCIALISE</h2>
      <div class="icon-tile">
        <svg width="229" height="166" viewBox="0 0 229 166" aria-label="Speech bubbles icon" role="img">
          <ellipse cx="98" cy="70" rx="56" ry="40" fill="#fbd2b8"/>
          <path d="M70 100 L60 130 L96 108 Z" fill="#fbd2b8"/>
          <ellipse cx="150" cy="104" rx="34" ry="24" fill="#fde3d3"/>
          <path d="M160 122 L170 142 L146 126 Z" fill="#fde3d3"/>
        </svg>
      </div>
    </div>
    <div class="banner__base"><span class="brand-name">LUMENVALE</span></div>
  </section>

  <section class="banner banner--inspire">
    <div class="banner__stage">
      <h2 class="banner__word">INSPIRE</h2>
      <div class="icon-tile">
        <div class="icon-tile__art" role="img" aria-label="Illustration of two hands shaping a light bulb"></div>
      </div>
    </div>
    <div class="banner__base"><span class="brand-name">LUMENVALE</span></div>
  </section>

  <section class="banner banner--cta">
    <div class="banner__stage">
      <p class="cta__lead">DISCOVER THE<br>POWER OF</p>
      <h2 class="cta__headline">PUBLIC<br>RELATIONS</h2>
      <a class="cta__button" href="https://www.lumenvale.co.nz">LEARN MORE</a>
    </div>
    <div class="banner__base"><span class="brand-name">LUMENVALE</span></div>
  </section>
</main>
</body>
</html>
```